Looking for a professional, clean and crisp business card

I am in the underground utilities industry and am just looking for a really impressive business card. I would like our card to be white with our symbol crisp and clear with it protruding. I also have a business partner that will require his name and info on the card once the design is set. I would like to have our website info on the card which is;
http://harbortrenchco.example/

Contact Information for Business Card

Website, contact name, number and email

```html
<!DOCTYPE html>
<html lang="en">
<head>
<meta charset="utf-8">
<title>Harbor Trench Co — Business Card</title>
<link rel="stylesheet" href="https://fonts.googleapis.com/css2?family=Bebas+Neue&display=swap">
<style>
  :root {
    --backdrop: #a9aeb0;
    --card: #f3f3f1;
    --card-edge: #1d3b8f;
    --ink: #1c1c1c;
    --name-blue: #2f5bb0;
    --title-red: #d8202a;
    --info-grey: #5a5a5a;
  }
  html, body {
    margin: 0;
    padding: 0;
    width: 1200px;
    height: 824px;
    overflow: hidden;
    background: var(--backdrop);
  }
  .card {
    position: absolute;
    left: 150px;
    top: 155px;
    width: 900px;
    height: 514px;
    background: var(--card);
    border-bottom: 3px solid var(--card-edge);
    box-shadow: 0 6px 18px rgba(0,0,0,0.18);
    font-family: "Bebas Neue", "Oswald", sans-serif;
  }
  .contact {
    position: absolute;
    left: 82px;
    top: 178px;
  }
  .contact-name {
    margin: 0;
    color: var(--name-blue);
    font-size: 50px;
    line-height: 1;
    font-weight: 400;
    letter-spacing: 0.5px;
  }
  .contact-title {
    margin: 2px 0 18px;
    color: var(--title-red);
    font-size: 26px;
    line-height: 1;
    letter-spacing: 0.5px;
  }
  .contact-lines {
    margin: 0 0 16px;
    color: var(--info-grey);
    font-size: 22px;
    line-height: 1.15;
    letter-spacing: 1px;
  }
  .brand {
    position: absolute;
    left: 470px;
    top: 0;
    width: 400px;
    height: 514px;
    display: flex;
    align-items: center;
    justify-content: center;
    gap: 18px;
  }
  .brand-dot {
    width: 34px;
    height: 34px;
    border-radius: 50%;
    background: var(--ink);
    flex: none;
  }
  .brand-name {
    color: var(--ink);
    font-size: 62px;
    line-height: 1;
    letter-spacing: 1px;
    white-space: nowrap;
  }
</style>
</head>
<body>
  <article class="card">
    <section class="contact">
      <h1 class="contact-name">Daniel Reyes</h1>
      <p class="contact-title">President</p>
      <p class="contact-lines">
        Harbor Trench Co LLC<br>
        4120 Alder Crest Road<br>
        Cedar Hollow, Alaska 99500
      </p>
      <p class="contact-lines">
        555-014-2297<br>
        info@harbortrenchco.example<br>
        www.harbortrenchco.example
      </p>
    </section>
    <div class="brand">
      <span class="brand-dot"></span>
      <span class="brand-name">Harbor Trench Co</span>
    </div>
  </article>
</body>
</html>
```